Exciting new branding of Recruitment Company based on it's new website

We have an exciting new website we are about to launch and would like to have letterhead, business cards, email signature options, email banner, linkedin and facebook cover images all refreshed to match the website. I have attached the existing logo. The website is at http://brightcrewstaff.hostpadsites.com/ and we are particularly interested in the grey with orange writing at the base of the first page where it says Register Now

Target Market(s)

Recruitment

Contact Information for Business Card

Dana Thorpe
Account Executive
T: 1300 582 318
M: 0412 736 085
E: dana@brightcrewstaff.com.au
W: brightcrewstaff.com.au
A: Suite 3, 42 Wattlebank Lane, Deakin ACT 2600
ABN: 52 184 637 905

Font styles to use
Serif
Sans Serif

Requirements
Must have
• The grey colour from the website

```html
<!DOCTYPE html>
<html lang="en">
<head>
<meta charset="utf-8">
<title>Brightcrew Staff – Business Card</title>
<link rel="stylesheet" href="https://fonts.googleapis.com/css2?family=Lato:wght@400;700;900&display=swap">
<style>
  :root {
    --brand-orange: #e27a26;
    --logo-orange: #efa64c;
    --text-grey: #58585a;
    --rule-grey: #9a9a9a;
    --border-grey: #a8a8a8;
    --paper: #ffffff;
  }
  html, body {
    margin: 0;
    padding: 0;
    width: 1045px;
    height: 1200px;
    overflow: hidden;
    background: var(--paper);
    font-family: "Lato", Arial, sans-serif;
  }
  .canvas {
    position: relative;
    width: 1045px;
    height: 1200px;
  }
  .card-face {
    position: absolute;
    left: 1px;
    width: 1041px;
    height: 586px;
    border: 1px solid var(--border-grey);
    box-sizing: border-box;
    background: var(--paper);
  }
  .card-front { top: 1px; }
  .card-back { top: 612px; border-color: #c8c8c8; }

  .wordmark {
    position: absolute;
    display: flex;
    align-items: center;
  }
  .wordmark-square {
    background: var(--logo-orange);
    flex: none;
  }
  .wordmark-name {
    color: var(--logo-orange);
    font-weight: 900;
    line-height: 0.95;
    letter-spacing: -0.5px;
  }
  .front-mark { left: 268px; top: 166px; }
  .front-mark .wordmark-square { width: 200px; height: 200px; margin-right: 36px; border-radius: 4px; }
  .front-mark .wordmark-name { font-size: 64px; }

  .back-mark { left: 115px; top: 212px; }
  .back-mark .wordmark-square { width: 124px; height: 124px; margin-right: 22px; border-radius: 3px; }
  .back-mark .wordmark-name { font-size: 38px; }

  .divider {
    position: absolute;
    left: 476px;
    top: 64px;
    width: 2px;
    height: 458px;
    background: var(--rule-grey);
  }

  .contact-block {
    position: absolute;
    left: 520px;
    top: 86px;
    color: var(--text-grey);
  }
  .person-name {
    margin: 0;
    font-size: 37px;
    font-weight: 700;
    color: var(--brand-orange);
    line-height: 44px;
  }
  .person-title {
    margin: 0 0 24px;
    font-size: 30px;
    font-weight: 400;
    line-height: 40px;
  }
  .contact-list {
    margin: 0;
    padding: 0;
    list-style: none;
    font-size: 30px;
    line-height: 41px;
  }
  .contact-row { display: flex; }
  .contact-label {
    color: var(--brand-orange);
    width: 46px;
    flex: none;
  }
  .contact-row.abn { margin-top: 11px; }
  .contact-row.abn .contact-label { width: auto; margin-right: 8px; }
</style>
</head>
<body>
<main class="canvas">
  <section class="card-face card-front">
    <div class="wordmark front-mark">
      <span class="wordmark-square"></span>
      <span class="wordmark-name">brightcrew<br>staff</span>
    </div>
  </section>

  <section class="card-face card-back">
    <div class="wordmark back-mark">
      <span class="wordmark-square"></span>
      <span class="wordmark-name">brightcrew<br>staff</span>
    </div>
    <div class="divider"></div>
    <div class="contact-block">
      <h1 class="person-name">Dana Thorpe</h1>
      <p class="person-title">Account Executive</p>
      <ul class="contact-list">
        <li class="contact-row"><span class="contact-label">T:</span><span>1300 582 318</span></li>
        <li class="contact-row"><span class="contact-label">M:</span><span>0412 736 085</span></li>
        <li class="contact-row"><span class="contact-label">E:</span><span>dana@brightcrewstaff.com.au</span></li>
        <li class="contact-row"><span class="contact-label">W:</span><span>brightcrewstaff.com.au</span></li>
        <li class="contact-row"><span class="contact-label">A:</span><span>Suite 3, 42 Wattlebank Lane,<br>Merrowdale ACT 2609</span></li>
        <li class="contact-row abn"><span class="contact-label">ABN:</span><span>52 184 637 905</span></li>
      </ul>
    </div>
  </section>
</main>
</body>
</html>
```